Modernising a Traditional Image - Velmar Brass Band

The Brass Band musical world in Britain is under threat. It is a wonderful place for children and amateurs to learn a musical instrument - it is our responsibility to protect it and grow it.
We can have a combined image of being old and slow. Our organisation wants to celebrate youth and a new / innovative way of doing things.

We don't wish to create a new logo as that exists now on our rather expensive uniforms - BUT to provide an attractive message for potential young players, something that we can use on Roll-up Banners, Facebook posts, Web banners, Tickets, Concert programmes. In short a cohesive image for our communication. I have however included the Logo design - so perhaps preparing the road for a future logo transition, or perhaps for use with the Velmar Academy / Training Band.

UPDATE TO BRIEF 26/08 - DO NOT PLEASE INCLUDE THE OLD LOGO AT ALL. THINK NEW, THINK BOLD, THINK BRIGHT, YOUNG, ETC.

The final designs need to communicate a basis of tradition, but a bright, young innovative future. Please consider the bright brass bands in UK (https://www.instagram.com/qrtwlx/), and those in the Netherlands, Scandinavia, etc.

Current website / socials:
https://www.facebook.com/Velmarband
https://www.facebook.com/NorthGlimwick
https://www.velmar-example.band/

Target Market(s)

Young learners of musical instrument. Followers of music events, theatre, et.

Industry/Entity Type

Music theatre education

Requirements
Must have
• An invite.. 'come witness the magic being made at Band Practice Thursdays'.. as an example
Nice to have
• Bright colour (not linked to current logo). Surprise me
Should not have
• Any link to old logo

```html
<!DOCTYPE html>
<html lang="en">
<head>
<meta charset="utf-8">
<title>Velmar Band – Band Practice Thursdays</title>
<link rel="stylesheet" href="https://fonts.googleapis.com/css2?family=Bebas+Neue&family=Montserrat:wght@800&family=Saira+Condensed:wght@600&display=swap">
<style>
  :root {
    --paper: #c9a56f;
    --paper-light: #d6b785;
    --paper-dark: #a9844f;
    --red: #c9401f;
    --orange: #df8411;
    --teal: #0e6a5f;
    --brown: #4a2a1c;
    --rule: #2e2219;
  }
  html, body { margin: 0; padding: 0; overflow: hidden; }
  body { width: 900px; height: 1200px; }
  .poster {
    position: relative;
    width: 900px;
    height: 1200px;
    overflow: hidden;
    background: radial-gradient(ellipse at 50% 45%, var(--paper-light) 0%, var(--paper) 55%, var(--paper-dark) 100%);
  }
  .stripes { position: absolute; left: 0; top: 0; }
  .headline {
    position: absolute;
    left: 0;
    width: 900px;
    margin: 0;
    text-align: center;
    font-family: "Bebas Neue", sans-serif;
    font-weight: 400;
    line-height: 1;
    white-space: nowrap;
  }
  .headline span { position: absolute; left: 0; width: 100%; }
  .headline .teal { color: var(--teal); }
  .headline .orange { color: var(--orange); }
  .line-1 { top: 312px; font-size: 80px; letter-spacing: 2px; }
  .line-2 { top: 383px; font-size: 124px; letter-spacing: 6px; }
  .line-3 { top: 486px; font-size: 124px; letter-spacing: 6px; }
  .line-4 { top: 621px; font-size: 93px; letter-spacing: 3px; }
  .line-5 { top: 691px; font-size: 93px; letter-spacing: 3px; }
  .invite {
    position: absolute;
    top: 802px; left: 0; width: 900px; margin: 0;
    text-align: center;
    font-family: "Bebas Neue", sans-serif;
    font-size: 44px; letter-spacing: 3px; line-height: 1;
    color: var(--orange);
    opacity: 0.9;
  }
  .frame { position: absolute; left: 0; top: 0; }
  .day {
    position: absolute;
    top: 1013px; right: 488px;
    margin: 0;
    text-align: right;
    font-family: "Montserrat", sans-serif;
    font-weight: 800;
    font-size: 42px;
    line-height: 42px;
    color: var(--brown);
  }
  .divider {
    position: absolute;
    left: 445px; top: 1008px;
    width: 3px; height: 94px;
    background: var(--brown);
  }
  .address {
    position: absolute;
    left: 471px; top: 1007px;
    margin: 0;
    font-family: "Saira Condensed", sans-serif;
    font-weight: 600;
    font-style: normal;
    font-size: 17px;
    line-height: 19px;
    letter-spacing: 2.2px;
    text-transform: uppercase;
    color: var(--brown);
  }
  .address .band-name { color: var(--teal); display: block; }
  .contact {
    position: absolute;
    top: 1115px; left: 0; width: 900px;
    display: flex; justify-content: center; align-items: center; gap: 12px;
    font-family: "Montserrat", sans-serif;
    font-weight: 800;
    font-size: 17px;
    color: var(--teal);
  }
  .contact .dot {
    width: 24px; height: 24px; border-radius: 50%;
    background: var(--teal);
    margin-left: 12px;
  }
  .contact .sep { width: 2px; height: 22px; background: var(--teal); }
</style>
</head>
<body>
<main class="poster">
  <svg class="stripes" width="900" height="270" viewBox="0 0 900 270">
    <rect x="0" y="41" width="900" height="50" fill="var(--red)"/>
    <rect x="0" y="91" width="900" height="56" fill="var(--orange)"/>
    <rect x="0" y="147" width="900" height="57" fill="var(--teal)"/>
    <rect x="0" y="204" width="900" height="46" fill="var(--brown)"/>
    <g stroke="var(--rule)" stroke-width="1.2">
      <line x1="0" y1="55" x2="900" y2="55"/>
      <line x1="0" y1="84" x2="900" y2="84"/>
      <line x1="0" y1="121" x2="900" y2="121"/>
      <line x1="0" y1="171" x2="900" y2="171"/>
      <line x1="0" y1="194" x2="900" y2="194"/>
      <line x1="0" y1="230" x2="900" y2="230"/>
    </g>
    <rect class="notes-art" role="img" aria-label="Musical notes and clefs cut out of the stripes" x="245" y="0" width="405" height="262" rx="30" fill="var(--paper)" opacity="0.85"/>
  </svg>

  <svg class="frame" width="900" height="1200" viewBox="0 0 900 1200" aria-hidden="true">
    <g stroke-width="1" stroke-dasharray="3 3">
      <line x1="44" y1="315" x2="44" y2="1090" stroke="var(--teal)"/>
      <line x1="857" y1="315" x2="857" y2="1090" stroke="var(--teal)"/>
      <line x1="200" y1="777" x2="752" y2="777" stroke="var(--teal)"/>
      <line x1="200" y1="867" x2="752" y2="867" stroke="var(--teal)"/>
    </g>
  </svg>

  <h1 class="headline">
    <span class="line-1 teal">We make</span>
    <span class="line-2 orange">Melodious</span>
    <span class="line-3 orange">Magic</span>
    <span class="line-4 teal">Happen in our</span>
    <span class="line-5 teal">Band practice!</span>
  </h1>

  <p class="invite">Come witness it!</p>

  <p class="day">EVERY<br>THURSDAY</p>
  <div class="divider"></div>
  <address class="address">
    <span class="band-name">Velmar Band,</span>
    North Glimwick Community Centre,<br>
    Ferrow Meadow, North Glimwick<br>
    Westmarch,<br>
    GL9 7QX
  </address>

  <div class="contact">
    <span class="web">www.velmar-example.band</span>
    <span class="dot"></span>
    <span class="social">Velmarband</span>
    <span class="sep"></span>
    <span class="social">NorthGlimwick</span>
  </div>
</main>
</body>
</html>
```